2-4 page graphic work for a press kit

I need a press kit designed for an app. This is a very simple presentation of the app with only a little text and a few pictures that the designer can choose from and use at will. There is a word document with the text, a few pictures, screenshots of the app as well as the logo. SImply follow the order of the text and put corresponding photos if you feel they apply.
If you want to add other pictures that is fine but they must follow the same theme which is basically things that you would do with your friends; lunch, go running, go to the museum, go to the movies etc.

```html
<!DOCTYPE html>
<html lang="en">
<head>
<meta charset="utf-8">
<title>pal loop — Press Kit</title>
<link rel="stylesheet" href="https://fonts.googleapis.com/css2?family=Quicksand:wght@400;500;700&display=swap">
<style>
  :root {
    --backdrop: #3b2f27;
    --teal: #5fe9d6;
    --teal-deep: #3fcdb9;
    --slate: #2a3a41;
    --slate-soft: #3a4b52;
    --yellow: #f6b530;
    --paper: #ffffff;
    --ink: #3d4b50;
    --ink-soft: #6b777b;
  }
  * { box-sizing: border-box; margin: 0; padding: 0; }
  html, body { width: 1200px; height: 514px; overflow: hidden; background: var(--backdrop); }
  body { font-family: "Quicksand", "Helvetica Neue", Arial, sans-serif; }

  .press-kit {
    width: 1200px; height: 514px;
    display: flex; justify-content: center; align-items: center; gap: 20px;
  }
  .page {
    position: relative; width: 218px; height: 330px; overflow: hidden;
    background: var(--paper);
    box-shadow: 0 6px 16px rgba(0,0,0,.45);
  }

  /* image areas */
  .visual { position: absolute; left: 0; top: 0; width: 100%; }

  /* section badge */
  .badge {
    position: absolute; left: 50%; transform: translateX(-50%);
    width: 50px; height: 50px; border-radius: 10px;
    background: var(--teal); border: 3px solid var(--paper);
    box-shadow: 0 1px 4px rgba(0,0,0,.25);
    display: flex; flex-direction: column; align-items: center; justify-content: center;
  }
  .badge svg { width: 22px; height: 22px; }
  .badge-label {
    font-size: 4.6px; color: var(--paper); letter-spacing: .3px;
    text-transform: uppercase; margin-top: 2px;
  }

  .copy {
    position: absolute; left: 16px; right: 16px;
    font-size: 4.4px; line-height: 1.45; text-align: center; color: var(--ink);
  }
  .copy p + p { margin-top: 5px; }

  /* footer */
  .footer-bar { position: absolute; left: 0; bottom: 8px; height: 6px; width: 80%; background: var(--slate); }
  .brand-tag {
    position: absolute; right: 8px; bottom: 4px;
    display: flex; align-items: center; gap: 3px;
    font-size: 9px; font-weight: 500; color: var(--slate);
  }
  .brand-tag .mark { width: 12px; height: 12px; border-radius: 3px; background: var(--teal); }

  /* cover */
  .cover .top { position: absolute; inset: 0 0 45% 0; background: var(--teal); }
  .cover .bottom { position: absolute; inset: 55% 0 0 0; background: var(--slate); }
  .cover .brand-name {
    position: absolute; top: 62px; width: 100%; text-align: center;
    font-size: 27px; font-weight: 500; color: var(--paper);
  }
  .cover .brand-square {
    position: absolute; left: 50%; top: 142px; transform: translateX(-50%);
    width: 60px; height: 60px; border-radius: 11px;
    background: var(--teal); border: 3px solid var(--paper);
  }
  .cover .tagline {
    position: absolute; left: 12px; right: 12px; top: 256px;
    border-top: 1px solid var(--teal); border-bottom: 1px solid var(--teal);
    padding: 6px 0; font-size: 6.2px; line-height: 1.35; letter-spacing: .4px;
    color: var(--teal); text-align: center; text-transform: uppercase;
  }

  /* idea */
  .idea { background: var(--teal); }
  .idea .visual { height: 150px; background: var(--yellow); }
  .idea .footer-bar { width: 86%; }

  /* founders */
  .founders .visual { height: 138px; background: linear-gradient(160deg, #8ab3c8 0%, #c9a78a 45%, #8c5b45 100%); }
  .founders .copy { color: var(--ink-soft); }

  /* concept */
  .concept { background: var(--slate); }
  .concept .visual { height: 168px; background: linear-gradient(180deg, #2d3d44 0 14px, #eef2f2 14px); }
  .concept .copy { color: var(--paper); text-align: left; }
  .concept .footer-bar { background: var(--paper); width: 74%; }
  .concept .brand-tag { color: var(--paper); }

  /* faqs */
  .faqs .visual { height: 140px; background: linear-gradient(180deg, #9fd2ee 0%, #c6e4f2 40%, #6aa8c4 58%, #e3cfa6 72%, #d9c29a 100%); }
  .faqs .copy { color: var(--ink-soft); }
  .faqs .question { color: var(--teal-deep); font-weight: 500; }
  .faqs .question + p { margin-top: 1px; }
</style>
</head>
<body>
<main class="press-kit">

  <section class="page cover">
    <div class="top"></div>
    <div class="bottom"></div>
    <div class="brand-name">pal loop</div>
    <div class="brand-square"></div>
    <p class="tagline">The app that connects you with new people and allows you to grow your social network</p>
  </section>

  <section class="page idea">
    <div class="visual" role="img" aria-label="Flat yellow illustration of a plug cord leading to a brain and a glowing light bulb"></div>
    <div class="badge" style="top:127px">
      <svg viewBox="0 0 24 24" fill="none" stroke="#fff" stroke-width="1.8" stroke-linecap="round">
        <path d="M8.5 15c-1.8-1.2-3-3.2-3-5.5a6.5 6.5 0 0 1 13 0c0 2.3-1.2 4.3-3 5.5v2h-7z"/>
        <path d="M9 19.5h6M10 22h4"/>
      </svg>
      <span class="badge-label">The Idea</span>
    </div>
    <div class="copy" style="top:198px">
      <p>Have you ever found yourself in the situation where you want to attend a concert, go to an art exhibition, explore a mountain trail or simply just try out a new café, but you have no one to come with you? Do you end up cancelling it?</p>
      <p>After having moved around between different cities and countries, the developers of pal loop encountered the pitfall of a limited social network and the difficulties of re-establishing social connections. During the period of lost experiences and cancelled plans, the idea behind pal loop came into light.</p>
    </div>
    <div class="footer-bar"></div>
    <div class="brand-tag"><span class="mark"></span>pal loop</div>
  </section>

  <section class="page founders">
    <div class="visual" role="img" aria-label="Photo of the two founders sharing lunch outdoors on a sunny terrace"></div>
    <div class="badge" style="top:114px">
      <svg viewBox="0 0 24 24" fill="none" stroke="#fff" stroke-width="2" stroke-linecap="round">
        <rect x="3" y="9" width="10" height="6" rx="3" transform="rotate(-45 8 12)"/>
        <rect x="11" y="9" width="10" height="6" rx="3" transform="rotate(-45 16 12)"/>
      </svg>
      <span class="badge-label">The Founders</span>
    </div>
    <div class="copy" style="top:182px">
      <p>Have you ever found yourself in the situation where you want to attend a concert, go to an art exhibition, explore a mountain trail or simply just try out a new café, but you have no one to come with you? Do you end up cancelling it?</p>
      <p>After having moved around between different cities and countries, the developers of pal loop encountered the pitfall of a limited social network and the difficulties of re-establishing social connections. During the period of lost experiences and cancelled plans, the idea behind pal loop came into light.</p>
    </div>
    <div class="footer-bar"></div>
    <div class="brand-tag"><span class="mark"></span>pal loop</div>
  </section>

  <section class="page concept">
    <div class="visual" role="img" aria-label="App screenshots showing the activity list and the publish activity form with date, time, cost and map"></div>
    <div class="badge" style="top:144px">
      <svg viewBox="0 0 24 24" fill="#fff">
        <path d="M5 10l7-7 8 8-7 7z"/>
        <path d="M19 14c1.2 1.8 2 3 2 4a2 2 0 0 1-4 0c0-1 .8-2.2 2-4z"/>
      </svg>
      <span class="badge-label">The Concept</span>
    </div>
    <div class="copy" style="top:208px">
      <p>Pal Loop is a platform where the users first automatically create a profile by logging in with their Friendbook account.</p>
      <p>Once the profile is set up, the user will immediately get access to the list of activities that will take place nearby. The user can also easily publish any activity, which again will be visible to users who are located nearby.</p>
      <p>In order to publish an activity, the user only needs to plot in a brief description of the activity, where to meet, as well as what date and time the activity will be carried out. The publisher also has to disclose if there are any costs that other participants will have to cover, such as an entrance fee.</p>
      <p>As soon as a user confirms that he or she will join a specific activity, a chat option will be available. This allows for communication and interaction between the users participating in the same activity. So simple, yet so enriching.</p>
    </div>
    <div class="footer-bar"></div>
    <div class="brand-tag"><span class="mark"></span>pal loop</div>
  </section>

  <section class="page faqs">
    <div class="visual" role="img" aria-label="Photo of a group of friends in wetsuits cheering on the beach with surfboards"></div>
    <div class="badge" style="top:116px">
      <svg viewBox="0 0 24 24" fill="none" stroke="#fff" stroke-width="1.8" stroke-linecap="round">
        <circle cx="12" cy="12" r="10"/>
        <path d="M9.2 9.3a2.9 2.9 0 1 1 4 2.7c-.8.4-1.2 1-1.2 1.9v.6"/>
        <circle cx="12" cy="17.4" r=".6" fill="#fff"/>
      </svg>
      <span class="badge-label">FAQs</span>
    </div>
    <div class="copy" style="top:186px">
      <p class="question">What do I need to start using Pal Loop?</p>
      <p>In order to become a user, you only need a Nimbus OS compatible device, internet connection and a Friendbook profile. Once the app is downloaded, you can easily create a user linked to your Friendbook profile. You can then enjoy the application right away.</p>
      <p class="question">How will I benefit from using Pal Loop?</p>
      <p>By being a user of Pal Loop, you will have naturally established a contact point with others in the same situation as you. It is our hope that Pal Loop will help you grow your social network when you want to meet new people.</p>
      <p class="question">How much does it cost to use Pal Loop?</p>
      <p>Pal Loop is completely free to use and we have no plans to start charging you.</p>
    </div>
    <div class="footer-bar"></div>
    <div class="brand-tag"><span class="mark"></span>pal loop</div>
  </section>

</main>
</body>
</html>
```